Business Cards and Stationary for High End Valet Dry Cleaning Service
Brightmere Garment Care "It's fresh pressing in crate!"
Use same font as used in my logo
The font for the business logo should not change. All other details please use your best judgement.
Professional
Dorian Velkoski
Director of Sales and Marketing
41 Parcell Lane
Toronto, Ontario
M5K 3R7
dorian@brightmeregarments.example
www.brightmeregarments.example
IMPORTANT INFORMATION:
Please read the below before starting your design.
Letterheads: I will require 2 sized letterheads with different pieces of information on each.
1st Letterhead:
Normal 8 ½ inches wide by 11 inches long US Letter.
Information to be included: Business Logo, Address, Number, and Web URL
2nd Letterhead:
Legal sized paper 8 ½ inches wide by 14 inches long.
Information to be included: Business Logo, Name, Job Title, Number, Email, and Web URL
IMPORTANT: The goal is to type on this letterhead, print out, fold it a series of times and place it in a 6 ½ inch wide by 3 5/8 inch long envelope. As such, the width of the letterhead must not exceed 6 inches. Please leave the length at 14 inches. Please center the letterhead accordingly and only allow for 6 inches in width.
Envelopes: I will require 2 sized envelopes with different pieces of information on each.
1st Envelope:
Standard envelope for a 8 ½ inch wide by 11 inch long letter sized document.
2nd Envelope:
6 ½ inch wide by 3 5/8 inch long. The front should be the business logo, the back use your discretion.
Order Form: I will require a revision of the existing order form. A PDF file has been attached. Please replace existing logo with the current logo. As per the footer, please keep existing phone number and Web URL but replace ‘orders@brightmeregarments.example’ with ‘dorian@brightmeregarments.example’. Also, where it reads ‘Company Name’ it should read ‘Company/Building Name’.
IMPORTANT: Each order form will be printed and folded and will be placed in a plastic casing measuring 4 inches wide by 2.5 inches in length. Please make the necessary adjustments without sacrificing any of the detail.
Email Signature: I would like an email signature with the following details: Logo, Name, Job Title, Number, Email, and Web URL.
Would like the entire logo to take the space. This includes the logo, tag line and the perforated lines.
This is the company logo.
This is the existing Order Form that needs revising. Please replace existing logo with new logo or some form of it. Please make amendment to the footer as follows: please keep the phone number, and web URL but replace 'orders@brightmeregarments.example' with 'dorian@brightmeregarments.example'. Please note: each order form should be 4 inches in width by 2.5 inches in length. These will be incased in a plastic accordingly.

```html
<!DOCTYPE html>
<html lang="en">
<head>
<meta charset="utf-8">
<title>Brightmere Garment Care – Stationery Set</title>
<link href="https://fonts.googleapis.com/css2?family=Cinzel:wght@600&family=Open+Sans:wght@400;600;700&display=swap" rel="stylesheet">
<style>
:root{
  --stage:#2b2b2d;
  --navy:#172a86;
  --royal:#3552c2;
  --orange:#f2a01f;
  --paper:#ffffff;
  --ink:#3a3a44;
  --muted:#9aa0b4;
  --gold:#e8c873;
}
*{margin:0;padding:0;box-sizing:border-box}
html,body{width:1200px;height:302px;overflow:hidden;background:var(--stage);font-family:"Open Sans",Arial,sans-serif;color:var(--ink)}
.canvas{position:relative;width:1200px;height:302px}
.piece{position:absolute;overflow:hidden;box-shadow:0 2px 6px rgba(0,0,0,.45)}
.blue{background:linear-gradient(135deg,var(--royal),var(--navy) 75%)}
.white{background:var(--paper)}
.brand{display:flex;align-items:center;gap:4px;font-family:"Cinzel",Georgia,serif;font-weight:600;color:var(--gold);white-space:nowrap}
.brand .dot{flex:none;border-radius:50%;border:1px solid var(--gold)}
.tagline{font-family:"Cinzel",Georgia,serif;font-weight:600;color:var(--gold);white-space:nowrap}
.tiny{font-size:3.4px;line-height:1.5;color:var(--ink)}
.tiny-w{font-size:3.4px;line-height:1.5;color:#fff}
.band-foot{position:absolute;left:0;right:0;bottom:0;height:9px;background:var(--navy);border-top:2px solid var(--orange);display:flex;align-items:center;justify-content:center}
.rule{height:1px;background:#d9dce6;margin:3px 0}
/* business card */
.card-main{left:12px;top:48px;width:175px;height:165px;display:flex;flex-direction:column;align-items:center;justify-content:center;gap:6px}
.card-main .brand{font-size:11px}
.card-main .brand .dot{width:12px;height:12px}
.card-main .tagline{font-size:8px}
.card-front{left:14px;top:222px;width:80px;height:45px;display:flex;flex-direction:column;align-items:center;justify-content:center;gap:2px}
.card-front .brand{font-size:5px}.card-front .brand .dot{width:5px;height:5px}
.card-front .tagline{font-size:3.4px}
.card-back{left:100px;top:222px;width:80px;height:45px;padding:5px}
.card-back .name{font-size:4.4px;font-weight:700;color:var(--navy)}
.card-back .band-foot{height:6px}
/* letterheads */
.letter{left:204px;top:48px;width:127px;height:235px}
.letter-head{height:44px;display:flex;flex-direction:column;justify-content:center;padding:0 8px;gap:2px}
.letter-head .brand{font-size:6.5px}.letter-head .brand .dot{width:7px;height:7px}
.letter-head .tagline{font-size:4px}
.letter-body{padding:8px 10px}
.letter-body p{margin-bottom:3px}
.signature{display:block;width:30px;height:8px;margin:4px 0 2px}
.legal{left:348px;top:48px;width:108px;height:235px}
.legal .letter-head{height:30px}
/* envelopes */
.env-flap{left:468px;top:60px;width:126px;height:88px}
.env-front{left:468px;top:155px;width:130px;height:128px}
.env-front .corner{position:absolute;left:7px;top:7px}
.env-front .corner .brand{font-size:5px;color:var(--navy)}
.env-front .corner .brand .dot{width:5px;height:5px;border-color:var(--navy)}
.small-flap{left:612px;top:66px;width:180px;height:80px}
.small-front{left:636px;top:156px;width:120px;height:58px;display:flex;flex-direction:column;align-items:center;justify-content:center;gap:3px}
.small-front .brand{font-size:7px}.small-front .brand .dot{width:7px;height:7px}
.small-front .tagline{font-size:4.5px}
.small-back{left:618px;top:222px;width:175px;height:62px}
.sig{left:812px;top:66px;width:172px;height:130px}
.sig-top{height:86px;display:flex;flex-direction:column;align-items:center;justify-content:center;gap:4px}
.sig-top .brand{font-size:9px}.sig-top .brand .dot{width:9px;height:9px}
.sig-top .tagline{font-size:5.5px}
.sig-bottom{padding:6px 10px}
.sig-bottom .name{font-size:5px;font-weight:700;color:var(--navy)}
.mini-back{left:812px;top:216px;width:172px;height:68px}
/* order form */
.order{left:1003px;top:48px;width:190px;height:240px}
.order-head{height:28px;display:flex;align-items:center;justify-content:space-between;padding:0 8px}
.order-head .brand{font-size:5.5px}.order-head .brand .dot{width:6px;height:6px}
.order-title{font-size:8px;font-weight:700;color:#fff}
.order-body{padding:6px 8px}
.field{display:flex;gap:4px;align-items:flex-end;font-size:3.6px;margin-bottom:4px}
.field span{flex:1;border-bottom:1px solid #c9cddb;height:4px}
.checks{display:flex;gap:6px;font-size:3.6px;margin:4px 0}
.checks i{display:inline-block;width:4px;height:4px;border:1px solid var(--navy);margin-right:2px;vertical-align:middle}
.note-box{position:absolute;right:8px;top:34px;width:50px;height:28px;border:1px solid #9fcf8f;background:#e9f6e2;font-size:3.6px;padding:2px}
.items{width:100%;border-collapse:collapse;font-size:3.6px;margin-top:6px}
.items td{border-bottom:1px solid #dde0ea;height:9px;padding-left:2px}
.items td.qty{width:24px;border-left:1px solid #dde0ea}
</style>
</head>
<body>
<main class="canvas">

  <section class="piece blue card-main" aria-label="Business card, logo side">
    <div class="brand"><span class="dot"></span>Brightmere Garment Care</div>
    <div class="tagline">"It's fresh pressing in crate!"</div>
  </section>

  <section class="piece blue card-front" aria-label="Business card front">
    <div class="brand"><span class="dot"></span>Brightmere Garment Care</div>
    <div class="tagline">"It's fresh pressing in crate!"</div>
  </section>

  <section class="piece white card-back" aria-label="Business card back">
    <div class="name">Dorian Velkoski</div>
    <div class="tiny">Director of Sales and Marketing</div>
    <div class="tiny">(416) 555-0148 · dorian@brightmeregarments.example</div>
    <div class="band-foot"></div>
  </section>

  <article class="piece white letter" aria-label="Letter size letterhead">
    <header class="letter-head blue">
      <div class="brand"><span class="dot"></span>Brightmere Garment Care</div>
      <div class="tagline">"It's fresh pressing in crate!"</div>
    </header>
    <div class="letter-body tiny">
      <p>Date</p>
      <p>Recipient Name<br>Street Address<br>City, Province</p>
      <p>Dear Recipient,</p>
      <p>Thank you for choosing our valet service for your garments.</p>
      <p>We collect, clean and return every order with care.</p>
      <p>Sincerely,</p>
      <svg class="signature" viewBox="0 0 30 8"><path d="M1 6 C5 0 7 8 10 3 S15 7 18 2 S24 6 29 3" fill="none" stroke="#333" stroke-width=".6"/></svg>
      <p>Dorian Velkoski</p>
    </div>
    <footer class="band-foot"><span class="tiny-w">41 Parcell Lane, Toronto, Ontario M5K 3R7 · (416) 555-0148 · www.brightmeregarments.example</span></footer>
  </article>

  <article class="piece white legal" aria-label="Legal size letterhead">
    <header class="letter-head blue">
      <div class="brand"><span class="dot"></span>Brightmere Garment Care</div>
    </header>
    <footer class="band-foot"><span class="tiny-w">Dorian Velkoski · (416) 555-0148 · www.brightmeregarments.example</span></footer>
  </article>

  <section class="piece env-flap" aria-label="Letter envelope back" style="box-shadow:none;overflow:visible">
    <svg width="126" height="88" viewBox="0 0 126 88">
      <defs><linearGradient id="flapA" x1="0" y1="0" x2="1" y2="1"><stop offset="0" stop-color="#3552c2"/><stop offset=".8" stop-color="#172a86"/></linearGradient></defs>
      <path d="M0 0 H126 V60 Q63 92 0 60 Z" fill="url(#flapA)"/>
      <path d="M0 60 Q63 92 126 60" fill="none" stroke="#f2a01f" stroke-width="1.5"/>
    </svg>
  </section>

  <section class="piece white env-front" aria-label="Letter envelope front">
    <div class="corner">
      <div class="brand"><span class="dot"></span>Brightmere Garment Care</div>
      <div class="tiny">41 Parcell Lane, Toronto, Ontario M5K 3R7</div>
    </div>
    <div class="band-foot"></div>
  </section>

  <section class="piece small-flap" aria-label="Small envelope back" style="box-shadow:none;overflow:visible">
    <svg width="180" height="80" viewBox="0 0 180 80">
      <defs><linearGradient id="flapB" x1="0" y1="0" x2="1" y2="1"><stop offset="0" stop-color="#3552c2"/><stop offset=".8" stop-color="#172a86"/></linearGradient></defs>
      <path d="M0 0 H180 V52 Q90 86 0 52 Z" fill="url(#flapB)"/>
      <path d="M0 52 Q90 86 180 52" fill="none" stroke="#f2a01f" stroke-width="1.5"/>
    </svg>
  </section>

  <section class="piece blue small-front" aria-label="Small envelope front">
    <div class="brand"><span class="dot"></span>Brightmere Garment Care</div>
    <div class="tagline">"It's fresh pressing in crate!"</div>
  </section>

  <section class="piece small-back" aria-label="Small envelope flap view" style="box-shadow:none;overflow:visible">
    <svg width="175" height="62" viewBox="0 0 175 62">
      <defs><linearGradient id="flapC" x1="0" y1="0" x2="1" y2="1"><stop offset="0" stop-color="#3552c2"/><stop offset=".8" stop-color="#172a86"/></linearGradient></defs>
      <rect width="175" height="62" fill="url(#flapC)"/>
      <path d="M0 0 L87 34 L175 0" fill="none" stroke="#f2a01f" stroke-width="1.2"/>
    </svg>
  </section>

  <section class="piece white sig" aria-label="Email signature">
    <div class="sig-top blue">
      <div class="brand"><span class="dot"></span>Brightmere Garment Care</div>
      <div class="tagline">"It's fresh pressing in crate!"</div>
    </div>
    <div class="sig-bottom">
      <div class="name">Dorian Velkoski</div>
      <div class="tiny">Director of Sales and Marketing</div>
      <div class="tiny">(416) 555-0148 · dorian@brightmeregarments.example</div>
    </div>
  </section>

  <section class="piece mini-back" aria-label="Envelope back" style="box-shadow:none;overflow:visible">
    <svg width="172" height="68" viewBox="0 0 172 68">
      <defs><linearGradient id="flapD" x1="0" y1="0" x2="1" y2="1"><stop offset="0" stop-color="#3552c2"/><stop offset=".8" stop-color="#172a86"/></linearGradient></defs>
      <rect width="172" height="68" fill="url(#flapD)"/>
      <path d="M0 0 L86 38 L172 0" fill="none" stroke="#f2a01f" stroke-width="1.2"/>
    </svg>
  </section>

  <article class="piece white order" aria-label="Order form">
    <header class="order-head blue">
      <div class="brand"><span class="dot"></span>Brightmere Garment Care</div>
      <div class="order-title">Order Form</div>
    </header>
    <div class="order-body">
      <div class="field" style="width:110px">Company/Building Name<span></span></div>
      <div class="field" style="width:110px">Contact<span></span></div>
      <div class="field" style="width:110px">Phone<span></span></div>
      <div class="field" style="width:110px">Date<span></span></div>
      <div class="checks"><label><i></i>Starch</label><label><i></i>Fold</label></div>
      <div class="note-box">Notes</div>
      <table class="items">
        <tr><td>Shirts</td><td class="qty"></td></tr>
        <tr><td>Pants</td><td class="qty"></td></tr>
        <tr><td>Suits</td><td class="qty"></td></tr>
        <tr><td>Dresses</td><td class="qty"></td></tr>
        <tr><td></td><td class="qty"></td></tr>
        <tr><td></td><td class="qty"></td></tr>
        <tr><td>Total</td><td class="qty"></td></tr>
      </table>
    </div>
    <footer class="band-foot"><span class="tiny-w">(416) 555-0148 · dorian@brightmeregarments.example · www.brightmeregarments.example</span></footer>
  </article>

</main>
</body>
</html>
```